Cafe Menu Required

We need a menu for our coffee shop.
I would like something very much the same as what I have attached.

I have attached a word doc with the items needed on the menu.

I have also attached our logo

I would like to print these on A3 size poster

Industry/Entity Type

Cafe

```html
<!DOCTYPE html>
<html lang="en">
<head>
<meta charset="utf-8">
<title>Ward Nine Canteen – Menu</title>
<link rel="stylesheet" href="https://fonts.googleapis.com/css2?family=PT+Serif:wght@400;700&display=swap">
<style>
  :root {
    --page: #e8e2d8;
    --board: #3b2a20;
    --board-dark: #2e2019;
    --board-light: #44322a;
    --red: #e41f26;
    --text: #f4efe8;
    --cream: #f3efe2;
    --rule: #d8d2c8;
  }
  * { margin: 0; padding: 0; box-sizing: border-box; }
  html, body { width: 1200px; height: 961px; overflow: hidden; }
  body {
    background: var(--page);
    font-family: "PT Serif", Georgia, serif;
    color: var(--text);
    position: relative;
  }
  .menu-board {
    position: absolute;
    left: 70px; top: 127px;
    width: 1060px; height: 748px;
    background: linear-gradient(175deg, var(--board-light) 0%, var(--board) 45%, var(--board-dark) 100%);
    box-shadow: 0 10px 18px rgba(0,0,0,.35);
  }
  .frame {
    position: absolute;
    left: 25px; top: 78px;
    width: 1010px; height: 642px;
    border: 6px solid var(--red);
    border-top: none;
  }
  .frame-top {
    position: absolute;
    top: 78px; height: 6px;
    background: var(--red);
  }
  .frame-top.left { left: 25px; width: 400px; }
  .frame-top.right { left: 600px; width: 435px; }
  .brand {
    position: absolute;
    left: 425px; top: 62px;
    width: 175px;
    display: flex; align-items: center; justify-content: center; gap: 8px;
    font-size: 16px; font-weight: 700; letter-spacing: .5px;
    line-height: 1.1; text-transform: uppercase;
    color: var(--text);
  }
  .brand-dot {
    width: 16px; height: 16px; border-radius: 50%;
    background: var(--red); flex: none;
  }
  .tagline {
    position: absolute;
    left: 0; width: 1095px; top: 165px;
    text-align: center;
    font-size: 22px; letter-spacing: .3px;
  }
  .tagline .dash { color: var(--red); }
  .photo {
    position: absolute;
    left: 843px; top: 38px;
    width: 200px; height: 165px;
    background: var(--cream);
    padding: 10px 10px 18px;
    transform: rotate(7deg);
    box-shadow: 2px 4px 6px rgba(0,0,0,.4);
  }
  .photo-fill {
    width: 100%; height: 100%;
    background: radial-gradient(ellipse at 50% 60%, #8a6a4c 0%, #4a3526 55%, #2c2018 100%);
  }
  .section-title {
    position: absolute;
    font-size: 22px; font-weight: 400;
    white-space: nowrap;
    display: flex; align-items: center; gap: 6px;
    padding-bottom: 4px;
    border-bottom: 1.5px solid var(--rule);
    letter-spacing: .3px;
    line-height: 1.2;
  }
  .section-title.small { font-size: 18px; font-weight: 700; }
  .cross-icon { width: 28px; height: 28px; flex: none; }
  .items { position: absolute; list-style: none; }
  .items li {
    display: flex; justify-content: space-between; align-items: center;
    font-size: 22px; white-space: nowrap;
    font-variant-numeric: lining-nums;
  }
  .hot { left: 87px; top: 268px; width: 377px; }
  .hot li { height: 29.4px; }
  .extras { left: 536px; top: 320px; width: 436px; }
  .extras li { height: 29.5px; }
  .cold { left: 531px; top: 524px; width: 442px; }
  .cold li { height: 30.2px; }
</style>
</head>
<body>
  <main class="menu-board">
    <div class="frame"></div>
    <div class="frame-top left"></div>
    <div class="frame-top right"></div>

    <div class="brand"><span class="brand-dot"></span><span>Ward Nine Canteen</span></div>

    <p class="tagline">COFFEE <span class="dash">–</span> CATERING <span class="dash">–</span> FOOD TO GO</p>

    <div class="photo"><div class="photo-fill" role="img" aria-label="Photo of two hands holding cups of latte art on a wooden table"></div></div>

    <h2 class="section-title" style="left:57px; top:224px; width:218px;">HOT BEVERAGES
      <svg class="cross-icon" viewBox="0 0 28 28" aria-hidden="true"><rect x="1" y="1" width="26" height="26" fill="#fff" stroke="#e41f26" stroke-width="2"/><path d="M14 5v18M5 14h18" stroke="#e41f26" stroke-width="3.5"/></svg>
    </h2>
    <ul class="items hot">
      <li><span>Espresso</span><span>3.5</span></li>
      <li><span>Piccolo</span><span>3.5</span></li>
      <li><span>Short Macchiato</span><span>4.0</span></li>
      <li><span>Long Macchiato</span><span>4.5</span></li>
      <li><span>Latte</span><span>4/4.5/5.5</span></li>
      <li><span>Cappucinno</span><span>4/4.5/5.5</span></li>
      <li><span>Flat White</span><span>4/4.50/5.50</span></li>
      <li><span>Long Black</span><span>4/4.50/5.50</span></li>
      <li><span>Hot Chocolate</span><span>4/4.50/5.50</span></li>
      <li><span>White Hot Chocolate</span><span>4/4.50/5.50</span></li>
      <li><span>Mocha</span><span>4.5/5.0/6.0</span></li>
      <li><span>White Choc Mocha</span><span>4.5/5.0/6.0</span></li>
      <li><span>Chai Latte</span><span>4.5/5.0/6.0</span></li>
      <li><span>Dirty Chai</span><span>5.0/5.5/6.5</span></li>
      <li><span>Selection of Teas</span><span>3.8</span></li>
    </ul>

    <h2 class="section-title" style="left:520px; top:267px; width:122px;">EXTRAS
      <svg class="cross-icon" viewBox="0 0 28 28" aria-hidden="true"><rect x="1" y="1" width="26" height="26" fill="#fff" stroke="#e41f26" stroke-width="2"/><path d="M14 5v18M5 14h18" stroke="#e41f26" stroke-width="3.5"/></svg>
    </h2>
    <ul class="items extras">
      <li><span>Extra Shot</span><span>0.5</span></li>
      <li><span>Decaf</span><span>0.5</span></li>
      <li><span>Syrups – Caramel/Hazelnut/Vanilla</span><span>0.5</span></li>
      <li><span>Soy</span><span>0.5</span></li>
      <li><span>Lactose free</span><span>0.5</span></li>
    </ul>

    <h2 class="section-title small" style="left:515px; top:470px; width:220px;">COLD BEVERAGES
      <svg class="cross-icon" viewBox="0 0 28 28" aria-hidden="true"><rect x="1" y="1" width="26" height="26" fill="#fff" stroke="#e41f26" stroke-width="2"/><path d="M14 5v18M5 14h18" stroke="#e41f26" stroke-width="3.5"/></svg>
    </h2>
    <ul class="items cold">
      <li><span>Iced Latte</span><span>4.5</span></li>
      <li><span>Iced Long Black</span><span>4.5</span></li>
      <li><span>Iced Coffee w/ice cream</span><span>6.0</span></li>
      <li><span>Iced Chocolate w/ice cream</span><span>6.0</span></li>
      <li><span>Coffee Frappe</span><span>6.0</span></li>
      <li><span>Mango Frappe</span><span>6.0</span></li>
    </ul>
  </main>
</body>
</html>
```